Renewable energy website needs a wordpress website

We are a Renewable Energy company specialising in Energy Management, LED Lights and Solar PV Systems based in Kuala Lumpur.
We need wordpress website designed to match our company identity.
We would like to stick with similar shades of blue & green as our logo and to keep it fresh and creative at the same time.

```html
<!DOCTYPE html>
<html lang="en">
<head>
<meta charset="utf-8">
<title>Verdara Energy – Solar Power Services</title>
<link rel="stylesheet" href="https://fonts.googleapis.com/css2?family=Nunito+Sans:wght@400;600;700;800&family=Open+Sans:wght@400;600&display=swap">
<style>
:root{
  --blue:#29a9e1;
  --blue-dark:#1b8fc9;
  --green:#8cc63f;
  --green-dark:#6aab2c;
  --green-text:#6cb33f;
  --ring-lime:#c5d92d;
  --ring-olive:#5e8c31;
  --ring-leaf:#7dc142;
  --heading:#555a60;
  --text:#5d6166;
  --field-border:#cfd3d6;
  --footer-top:#b7c7e1;
  --footer-bottom:#97acd2;
  --footer-text:#5f6f95;
  --white:#ffffff;
}
*{box-sizing:border-box;margin:0;padding:0}
html,body{width:1024px;height:1200px;overflow:hidden}
body{position:relative;background:#fafbfb;font-family:"Nunito Sans",sans-serif;color:var(--text)}
.abs{position:absolute}

/* header */
.top-line{left:0;top:0;width:1024px;height:4px;background:var(--blue)}
.license-tab{left:704px;top:4px;width:196px;height:25px;background:var(--blue);color:var(--white);font-size:10px;font-weight:700;letter-spacing:.4px;display:flex;align-items:center;justify-content:center;border-radius:0 0 4px 10px}
.brand-name{font-weight:800;letter-spacing:2px;line-height:1.05}
.header-brand{left:160px;top:32px;color:var(--blue);font-size:21px}
.call-now{left:445px;top:42px;display:flex;align-items:center;gap:8px;font-size:19px;font-weight:800;color:#5a5f66}
.call-now .num{color:var(--green)}
.quote-btn{left:777px;top:39px;width:117px;height:29px;background:linear-gradient(#45bbee,var(--blue-dark));border:1px solid #1a89c0;color:var(--white);font-size:9.5px;font-weight:800;display:flex;align-items:center;justify-content:center;gap:5px}

/* nav */
.main-nav{left:0;top:96px;width:1024px;height:42px;background:linear-gradient(#9ad04f,#79b836);border-bottom:1px solid #5f9a2a}
.main-nav a{position:absolute;top:0;height:42px;line-height:42px;color:var(--white);font-weight:800;font-size:12.5px;text-decoration:none;transform:translateX(-50%);text-shadow:0 1px 1px rgba(0,0,0,.25)}
.main-nav a.active{left:183px;width:94px;text-align:center;background:linear-gradient(#43b7ec,#1e93cc)}

/* hero */
.hero{left:0;top:138px;width:1024px;height:274px;background:linear-gradient(160deg,#f3f6fb 0%,#9fb9e0 25%,#5a6fb7 55%,#8ea9d8 80%,#dbe6f4 100%)}
.hero-band{left:0;top:364px;width:650px;height:48px;background:rgba(140,198,63,.93);color:var(--white);font-size:22px;font-weight:800;line-height:48px;padding-left:135px;letter-spacing:-.2px}

/* quote panel */
.quote-panel{left:649px;top:157px;width:249px;height:447px}
.quote-title{left:649px;top:165px;width:249px;text-align:center;color:var(--white);font-weight:800;line-height:1}
.quote-title .small{font-size:18px;display:block}
.quote-title .big{font-size:26px;display:block;margin-top:2px}
.quote-lead{left:649px;top:243px;width:249px;text-align:center;font-family:"Open Sans",sans-serif;font-size:10px;font-weight:600;color:#333}
.field{left:665px;width:217px;height:32px;background:var(--white);border:1px solid var(--field-border);border-radius:2px;font-family:"Open Sans",sans-serif;font-size:9.5px;color:#777;padding:0 11px;line-height:30px;box-shadow:inset 0 1px 2px rgba(0,0,0,.06)}
.field.message{height:82px}
.select-arrow{right:8px;top:9px;width:11px;height:11px;background:#b8c8e6;border:1px solid #8fa6d2}
.submit-btn{left:700px;top:530px;width:143px;height:34px;background:linear-gradient(#4cc0f1,#1e94cd);border:1px solid #1a88bf;color:var(--white);font-size:17px;font-weight:800;display:flex;align-items:center;justify-content:center}

/* content */
.section-title{font-size:18px;font-weight:700;color:var(--heading)}
.body-copy{font-size:10px;line-height:16px;color:var(--text)}
.photo{background:linear-gradient(135deg,#d9dde2,#5d6f86 60%,#f2c230)}
.service{width:160px;text-align:center}
.service-label{font-size:12px;font-weight:700;color:var(--green-text);margin-top:10px}
.checklist{left:394px;top:822px;list-style:none}
.checklist li{display:flex;align-items:center;gap:10px;height:27px;font-size:10px;color:#555}
.partners{left:136px;top:950px;display:flex;gap:22px;align-items:center}
.partner{height:34px;background:#d6d8da;border-radius:3px}

/* side boxes */
.feature{left:651px;width:240px;height:109px;background:var(--green);color:var(--white)}
.feature .feature-photo{position:absolute;left:0;top:0;width:96px;height:109px;background:linear-gradient(#a6d35f,#4b6fa3)}
.feature .copy{position:absolute;left:102px;top:16px}
.feature .lead{font-size:22px;font-weight:800;line-height:1}
.feature .sub{font-size:13px;font-style:italic;font-weight:400;margin-top:2px}
.feature .tag{font-size:9.5px;font-weight:800;letter-spacing:.5px;line-height:13px;margin-top:14px}

/* footer */
.footer{left:0;top:1016px;width:1024px;height:160px;background:linear-gradient(var(--footer-top),var(--footer-bottom))}
.footer-brand{left:136px;top:1078px;color:var(--white);font-size:19px}
.footer-head{font-size:13px;font-weight:700;color:#7c8cae;letter-spacing:.5px}
.footer-list{list-style:none;font-size:9px;color:var(--footer-text)}
.footer-list li{height:19px;display:flex;align-items:center;gap:10px}
.contact-list li{height:auto;margin-bottom:9px;align-items:flex-start}
.map{left:649px;top:1048px;width:239px;height:102px;background:linear-gradient(135deg,#e6e2d6,#f0e9a0 45%,#e3dfd4)}
.bottom-bar{left:0;top:1176px;width:1024px;height:24px;background:linear-gradient(#33ace2,#1f8fcc);font-size:8.5px;color:#c9e9f8;line-height:24px}
</style>
</head>
<body>

<!-- header -->
<div class="abs top-line"></div>
<div class="abs license-tab">CONTRACT LICENSE # VR 48210</div>
<div class="abs brand-name header-brand">VERDARA<br>ENERGY</div>
<div class="abs call-now">
  <svg width="18" height="18" viewBox="0 0 18 18"><rect x="1" y="1" width="16" height="16" rx="2" fill="none" stroke="#6a6f75" stroke-width="1.5"/><path d="M6 4.5c-1 .5-1.5 2 0 4.5s3.5 4 5 3.5l1-1.5-2-1.5-1 .8c-.8-.4-1.8-1.5-2.2-2.3l.8-1L7 4.5z" fill="#6a6f75"/></svg>
  <span>CALL NOW:</span><span class="num">+60 3 8842 1907</span>
</div>
<div class="abs quote-btn">
  <svg width="10" height="8" viewBox="0 0 10 8"><rect x=".5" y=".5" width="9" height="7" fill="none" stroke="#fff"/><path d="M.5 .5l4.5 4 4.5-4" fill="none" stroke="#fff"/></svg>
  REQUEST A QUOTE
</div>

<!-- navigation -->
<nav class="abs main-nav">
  <a class="active" href="#">HOME</a>
  <a href="#" style="left:309px">SERVICES</a>
  <a href="#" style="left:446px">OUR TEAM</a>
  <a href="#" style="left:587px">ABOUT US</a>
  <a href="#" style="left:735px">CONTACT US</a>
</nav>

<!-- hero -->
<div class="abs hero" role="img" aria-label="Photo of solar panels under a bright sun and blue sky"></div>
<div class="abs hero-band">We Provide High-Standard Solar Power Services</div>

<!-- quote form -->
<svg class="abs quote-panel" viewBox="0 0 249 447" aria-hidden="true">
  <path d="M2 10 Q2 2 10 2 H239 Q247 2 247 10 V415 L124 445 L2 415 Z" fill="#fff" stroke="#e2e4e6"/>
  <path d="M2 10 Q2 2 10 2 H239 Q247 2 247 10 V56 L124 80 L2 56 Z" fill="#8cc63f"/>
</svg>
<div class="abs quote-title"><span class="small">GET A QUOTATION</span><span class="big">FOR FREE!</span></div>
<div class="abs quote-lead">Please select a service from below</div>
<div class="abs field" style="top:264px">Commercial Maintenance<span class="abs select-arrow"></span></div>
<div class="abs field" style="top:307px">Name</div>
<div class="abs field" style="top:350px">Email</div>
<div class="abs field" style="top:394px">Phone</div>
<div class="abs field message" style="top:437px">Message</div>
<div class="abs submit-btn">Submit Now</div>

<!-- welcome -->
<h2 class="abs section-title" style="left:138px;top:450px">Welcome to Verdara Energy</h2>
<p class="abs body-copy" style="left:142px;top:489px;width:356px">It is a long established fact that a reader will be distracted by the readable content of a page when looking at its layout. The point of using Lorem Ipsum is that it has a more-or-less normal distribution of letters, as opposed to using 'Content here, content here', making it look like readable English.</p>
<div class="abs photo" style="left:514px;top:491px;width:112px;height:69px" role="img" aria-label="Photo of a technician in a yellow hard hat"></div>

<!-- services -->
<div class="abs service" style="left:123px;top:589px">
  <svg width="130" height="130" viewBox="0 0 130 130" role="img" aria-label="Energy management icon"><circle cx="65" cy="65" r="56" fill="#fff" stroke="var(--ring-lime)" stroke-width="18"/></svg>
  <div class="service-label">Energy&nbsp; Management</div>
</div>
<div class="abs service" style="left:302px;top:589px">
  <svg width="130" height="130" viewBox="0 0 130 130" role="img" aria-label="LED lights icon"><circle cx="65" cy="65" r="56" fill="#fff" stroke="var(--ring-olive)" stroke-width="18"/></svg>
  <div class="service-label">LED Lights</div>
</div>
<div class="abs service" style="left:478px;top:586px">
  <svg width="130" height="130" viewBox="0 0 130 130" role="img" aria-label="Solar PV systems icon"><circle cx="65" cy="65" r="56" fill="#fff" stroke="var(--ring-leaf)" stroke-width="18"/></svg>
  <div class="service-label" style="margin-top:13px">Solar PV Systems</div>
</div>

<!-- why choose us -->
<h2 class="abs section-title" style="left:138px;top:779px">Why Choose Us</h2>
<p class="abs body-copy" style="left:137px;top:817px;width:242px">It is a long established fact that a reader will be distracted by the readable content of a page when looking at its layout. The point of using Lorem Ipsum is that it has a more-or-less normal distribution of letters, as opposed to using 'Content here, content here', making it look like readable English.</p>
<ul class="abs checklist">
  <li><svg width="14" height="14" viewBox="0 0 14 14"><circle cx="7" cy="7" r="7" fill="#8cc63f"/><path d="M6 4l3 3-3 3" fill="none" stroke="#fff" stroke-width="1.6"/></svg>Lorem ipsum dolor sit amet, consectetur</li>
  <li><svg width="14" height="14" viewBox="0 0 14 14"><circle cx="7" cy="7" r="7" fill="#8cc63f"/><path d="M6 4l3 3-3 3" fill="none" stroke="#fff" stroke-width="1.6"/></svg>Adipisicing elit, sed do eiusmod tempor</li>
  <li><svg width="14" height="14" viewBox="0 0 14 14"><circle cx="7" cy="7" r="7" fill="#8cc63f"/><path d="M6 4l3 3-3 3" fill="none" stroke="#fff" stroke-width="1.6"/></svg>Fncididunt ut labore et dolore magna</li>
  <li><svg width="14" height="14" viewBox="0 0 14 14"><circle cx="7" cy="7" r="7" fill="#8cc63f"/><path d="M6 4l3 3-3 3" fill="none" stroke="#fff" stroke-width="1.6"/></svg>Cliqua. Ut enim ad minim veniamquis</li>
</ul>
<div class="abs partners" aria-label="Partner companies">
  <span class="partner" style="width:82px"></span>
  <span class="partner" style="width:118px"></span>
  <span class="partner" style="width:82px"></span>
  <span class="partner" style="width:140px"></span>
</div>

<!-- side features -->
<div class="abs feature" style="top:626px">
  <div class="feature-photo" role="img" aria-label="Photo of a smiling technician holding a wrench"></div>
  <div class="copy"><div class="lead">30 YEARS</div><div class="sub">of experience.</div><div class="tag">GUARANTEED QUALITY<br>SERVICE</div></div>
</div>
<div class="abs feature" style="top:755px">
  <svg class="abs" style="left:23px;top:22px" width="64" height="64" viewBox="0 0 64 64" aria-hidden="true"><circle cx="32" cy="32" r="30" fill="#3d6b2f"/></svg>
  <div class="copy" style="top:28px"><div class="lead">GEA<br>MEMBER</div></div>
</div>
<div class="abs feature" style="top:886px">
  <div class="feature-photo" role="img" aria-label="Photo of a friendly support agent with a headset"></div>
  <div class="copy" style="top:20px"><div class="lead">0128 30416</div><div class="sub">Call us today</div><div class="tag" style="margin-top:12px">WE'LL BE GLAD TO<br>ASSIST YOU.</div></div>
</div>

<!-- footer -->
<footer class="abs footer"></footer>
<div class="abs brand-name footer-brand">VERDARA<br>ENERGY</div>
<h3 class="abs footer-head" style="left:376px;top:1047px">NAVIGATION</h3>
<ul class="abs footer-list" style="left:378px;top:1070px">
  <li><svg width="4" height="6" viewBox="0 0 4 6"><path d="M0 0l4 3-4 3z" fill="#6d7ea3"/></svg>Services</li>
  <li><svg width="4" height="6" viewBox="0 0 4 6"><path d="M0 0l4 3-4 3z" fill="#6d7ea3"/></svg>Our Team</li>
  <li><svg width="4" height="6" viewBox="0 0 4 6"><path d="M0 0l4 3-4 3z" fill="#6d7ea3"/></svg>Warranty Agent</li>
  <li><svg width="4" height="6" viewBox="0 0 4 6"><path d="M0 0l4 3-4 3z" fill="#6d7ea3"/></svg>Contact</li>
</ul>
<h3 class="abs footer-head" style="left:501px;top:1047px">CONTACT</h3>
<ul class="abs footer-list contact-list" style="left:504px;top:1078px">
  <li><svg width="10" height="14" viewBox="0 0 10 14"><path d="M5 0a5 5 0 015 5c0 4-5 9-5 9S0 9 0 5a5 5 0 015-5z" fill="#6d7ea3"/><circle cx="5" cy="5" r="2" fill="#b3c3de"/></svg><span>PO Box 5270<br>Kuala Lumpur</span></li>
  <li><svg width="11" height="8" viewBox="0 0 11 8"><rect width="11" height="8" fill="#6d7ea3"/><path d="M0 0l5.5 4.5L11 0" fill="none" stroke="#b3c3de"/></svg><span>hello@verdaraenergy.my</span></li>
  <li><svg width="11" height="11" viewBox="0 0 11 11"><path d="M2 0c-2 1-2 4 1 7s6 4 8 1l-2-2-1.5 1C6 6.5 4.5 5 4 4l1-1.5z" fill="#6d7ea3"/></svg><span>+1800 552 0193</span></li>
</ul>
<div class="abs map" role="img" aria-label="Street map showing the office location in the city centre"></div>

<div class="abs bottom-bar">
  <span class="abs" style="left:132px">Copyright 2014 © Company Site - All Rights Reserved</span>
  <span class="abs" style="left:777px">Site Map &nbsp;&nbsp;•&nbsp;&nbsp; Privacy Policy</span>
</div>

</body>
</html>
```